Poster for Dance Choreography Workshop

We need a poster for a dance workshop. This workshop is unique in that instead of focusing on dance technique or on classical compositional practices, it teaches participants a toolbox of a collaborative, improvisational methods for generating movement and creating dances.

The workshop is called VERIL (Methods for Exploring Gesture and Dancemaking). Our dance company is Helen Dorsey & Ensemble.

Here is copy:
VERIL (Methods for Exploring Gesture and Dancemaking) is a six-day intensive led by Helen Dorsey & Ensemble in which dancers and choreographers investigate collaborative approaches to choreography. Each day begins with an hour-long presentation during which Helen Dorsey leads discussions on topics related to choreography and collaboration. Following this, Helen Dorsey and VERIL company members teach a variety of practices for collaborative movement-making that merge improvisational skills with contemporary dance technique and physical theater. Using these practices, participants will create miniature compositions in small groups each day. By examining and discussing these creations, participants leave with greater confidence in their creative abilities and a deeper understanding of composition and movement-making.
This intensive, hosted at Whitcombe College in NYC, brings together a wide variety of talented dance artists and provides them with a supportive environment in which to play, learn, experiment and share. The intensive also affords an exciting opportunity for building peer-communities and forging new creative bonds. VERIL’s goal is that all participants leave with fresh perspectives, tools they can immediately use in their own rehearsals, and a better understanding of their own creative processes.

DATES:
June 11—June 16, 2012
10:00am—6:00pm daily
LOCATION:
Department of Dance,
Whitcombe College of
Harrowgate University
4127 Linden Avenue at 82nd
New York, NY 10094
Housing is not available.
Company teachers:
Helen Dorsey
Maribeth Quennell
Owen Patch
Toby Renfield

Special presentation by
Greta L. Fenwick,
Tall Stage Collective

Applications available online at www.helendorseyensemble.org or email veril@verilworks.org.
Application deadline April 1, 2012.

Hello all,

Nice work so far!
Please note that I have high resolution version of the images in the brief available. I did not include them because of the bandwidth of my connection. If you would like some of the images in higher res (5616x3744) let me know and I can provide them.

Best,

Colin

Target Market(s)

College-age and above. Professional dancers.

Industry/Entity Type

Environment

Requirements
Must have
• Poster must be 11x17 or smaller.
Visit www.northernmovementfair.org, www.pkthf.org, www.vlxmotion.org for competitors. Should not be easy to confuse with these.

```html
<!DOCTYPE html>
<html lang="en">
<head>
<meta charset="utf-8">
<title>VERIL Workshop Poster</title>
<link rel="stylesheet" href="https://fonts.googleapis.com/css2?family=Oswald:wght@400;500;700&display=swap">
<style>
  :root {
    --bg-light: #fbf6b8;
    --bg-mid: #efe27a;
    --bg-deep: #d9c63a;
    --plum: #5a1f5e;
    --magenta: #b0237e;
    --glow: #f6c9c2;
    --stripe: rgba(255, 255, 255, 0.75);
    --ghost: rgba(255, 255, 255, 0.78);
  }
  html, body {
    margin: 0;
    padding: 0;
    overflow: hidden;
    background: #ffffff;
  }
  .poster {
    position: relative;
    width: 778px;
    height: 1200px;
    overflow: hidden;
    font-family: "Oswald", "Arial Narrow", sans-serif;
    background: radial-gradient(ellipse 60% 45% at 50% 40%, var(--bg-light) 0%, var(--bg-mid) 55%, var(--bg-deep) 100%);
    color: var(--plum);
  }
  .poster p, .poster h1, .poster h2, .poster ul { margin: 0; }
  .stripes {
    position: absolute;
    left: 320px;
    top: 220px;
    width: 380px;
    height: 430px;
  }
  .dancer-photo {
    position: absolute;
    left: 270px;
    top: 290px;
    width: 340px;
    height: 520px;
    border-radius: 50%;
    background: radial-gradient(ellipse at 50% 45%, var(--glow) 0%, rgba(236, 150, 150, 0.55) 40%, rgba(239, 226, 122, 0) 72%);
  }
  .ghost-name {
    position: absolute;
    top: 18px;
    left: 0;
    width: 100%;
    text-align: center;
    font-size: 140px;
    font-weight: 700;
    letter-spacing: 10px;
    color: var(--ghost);
    line-height: 1;
  }
  .presenter {
    position: absolute;
    top: 6px;
    width: 100%;
    text-align: center;
    font-size: 24px;
    line-height: 32px;
    font-weight: 500;
    color: var(--plum);
  }
  .title-upper {
    position: absolute;
    top: 54px;
    width: 100%;
    text-align: center;
    font-size: 30px;
    line-height: 36px;
    font-weight: 500;
    color: var(--magenta);
    text-transform: uppercase;
  }
  .title-main {
    position: absolute;
    top: 90px;
    width: 100%;
    text-align: center;
    font-size: 40px;
    line-height: 48px;
    font-weight: 700;
    color: var(--plum);
    text-transform: uppercase;
  }
  .title-tag {
    position: absolute;
    top: 138px;
    right: 40px;
    font-size: 18px;
    line-height: 24px;
    color: var(--magenta);
    text-transform: uppercase;
  }
  .teachers {
    position: absolute;
    left: 80px;
    top: 170px;
  }
  .special {
    position: absolute;
    left: 56px;
    top: 456px;
  }
  .label {
    font-size: 27px;
    line-height: 34px;
    font-weight: 700;
    text-transform: uppercase;
    color: var(--plum);
  }
  .names {
    list-style: none;
    padding: 0 0 0 30px;
    font-size: 26px;
    line-height: 30px;
    font-weight: 500;
    color: var(--magenta);
  }
  .special .names { padding-left: 46px; }
  .details {
    position: absolute;
    top: 818px;
    width: 100%;
    text-align: center;
    text-transform: uppercase;
  }
  .dates {
    font-size: 44px;
    line-height: 50px;
    font-weight: 700;
    color: var(--plum);
  }
  .hours {
    font-size: 28px;
    line-height: 32px;
    color: var(--plum);
  }
  .venue {
    font-size: 26px;
    line-height: 30px;
    font-weight: 700;
    color: var(--magenta);
  }
  .address {
    font-size: 26px;
    line-height: 34px;
    font-weight: 500;
    color: var(--plum);
  }
  .notes {
    text-transform: none;
    font-size: 13px;
    line-height: 17px;
    color: var(--plum);
  }
  .notes-caps { text-transform: uppercase; }
  .competitors {
    margin-top: 4px !important;
    font-size: 20px;
    line-height: 24px;
    color: var(--magenta);
  }
  .competitors span {
    display: block;
    text-transform: none;
  }
</style>
</head>
<body>
<main class="poster">
  <svg class="stripes" viewBox="0 0 380 430" aria-hidden="true">
    <rect x="0" y="0" width="380" height="26" fill="var(--stripe)"/>
    <rect x="0" y="54" width="380" height="26" fill="var(--stripe)"/>
    <rect x="0" y="108" width="380" height="26" fill="var(--stripe)"/>
    <rect x="0" y="162" width="380" height="26" fill="var(--stripe)"/>
    <rect x="0" y="216" width="380" height="26" fill="var(--stripe)"/>
    <rect x="0" y="270" width="380" height="26" fill="var(--stripe)"/>
    <rect x="0" y="324" width="380" height="26" fill="var(--stripe)"/>
    <rect x="0" y="378" width="380" height="26" fill="var(--stripe)"/>
  </svg>

  <div class="dancer-photo" role="img" aria-label="Photograph of a dancer leaping mid-movement in a warm pink glow"></div>

  <div class="ghost-name" aria-hidden="true">VERIL</div>
  <p class="presenter">Helen Dorsey &amp; Ensemble Presents</p>
  <h1>
    <span class="title-upper">Methods for Exploring</span>
    <span class="title-main">Gesture and Dancemaking</span>
  </h1>
  <span class="title-tag">Workshop</span>

  <section class="teachers">
    <h2 class="label">Company Teachers</h2>
    <ul class="names">
      <li>Helen Dorsey</li>
      <li>Maribeth Quennell</li>
      <li>Owen Patch</li>
      <li>Toby Renfield</li>
    </ul>
  </section>

  <section class="special">
    <h2 class="label">Special Presentation By</h2>
    <ul class="names">
      <li>Greta L. Fenwick,</li>
      <li>Tall Stage Collective</li>
    </ul>
  </section>

  <section class="details">
    <p class="dates">From June 11 to June 16, 2012</p>
    <p class="hours">10:00 AM to 6:00 PM</p>
    <p class="venue">At the Department of Dance</p>
    <p class="venue">Whitcombe College of Harrowgate University</p>
    <p class="address">4127 Linden Avenue at 82nd New York, NY 10094</p>
    <p class="notes notes-caps">Housing is not available</p>
    <p class="notes">Applications available online at:</p>
    <p class="notes">www.helendorseyensemble.org</p>
    <p class="notes">veril@verilworks.org</p>
    <p class="notes">Application deadline April 1, 2012.</p>
    <p class="competitors">For competitors visit
      <span>www.northernmovementfair.org</span>
      <span>www.pkthf.org</span>
      <span>www.vlxmotion.org</span>
    </p>
  </section>
</main>
</body>
</html>
```